Brightleaf Oruma needs a new label design for our Kombucha range- 5 Flavours

We need a label design for our Kombucha range. We are looking for a new look that says quality, vibrant, modern, energetic. The design should draw from our brand identity and the Zanzibar landscape, while communicating internationally. We need a label that describes us and catches the consumer's eye as they scan the supermarket shelves.
Each label should have the same design foundation- with a slight difference in colour to reflect the Kombucha Flavour. Our flavours are: Classic, Ginger/Turmeric, Hibiscus, Cinammon/Clove and Lemongrass.
I have attached in order: our current label (all info on label will remain the same), screenshots from our brand book, some images of labels we love. Our kombucha is packed in glass bottles- it may be nice to play with clear cut outs that bring out the colour of the beverage within the label design.
Check us out on Instagram @brightleaforuma for the vibe

```html
<!DOCTYPE html>
<html lang="en">
<head>
<meta charset="utf-8">
<title>Brightleaf Oruma Kombucha Labels</title>
<link rel="stylesheet" href="https://fonts.googleapis.com/css2?family=Bebas+Neue&family=Oswald:wght@300;400;600&family=Montserrat:wght@600;700&family=Yellowtail&display=swap">
<style>
  :root {
    --page: #ffffff;
    --paper: #f4f4f4;
    --ink: #161616;
    --band-text: #ffffff;
    --lemongrass: #8cc63f;
    --lemongrass-deep: #5b9a1e;
    --ginger: #e8892a;
    --ginger-deep: #c8651a;
    --hibiscus: #e3262e;
    --hibiscus-deep: #c8161d;
    --cinnamon: #9c6b45;
    --cinnamon-deep: #7a4e2e;
    --classic: #f0cc2a;
    --classic-deep: #d9b21c;
  }
  * { box-sizing: border-box; margin: 0; padding: 0; }
  ul { list-style: none; }
  html, body { width: 1200px; height: 1200px; overflow: hidden; background: var(--page); }
  .range {
    width: 1200px; height: 1200px;
    display: flex; justify-content: center; align-items: center; gap: 14px;
  }
  .label {
    width: 220px; height: 480px;
    background: var(--paper);
    border: 1px solid #e2e2e2;
    display: flex; flex-direction: column; align-items: center;
    padding-top: 34px;
    color: var(--ink);
    font-family: 'Oswald', sans-serif;
    overflow: hidden;
  }
  .label--lemongrass { --accent: var(--lemongrass); --accent-deep: var(--lemongrass-deep); }
  .label--ginger { --accent: var(--ginger); --accent-deep: var(--ginger-deep); }
  .label--hibiscus { --accent: var(--hibiscus); --accent-deep: var(--hibiscus-deep); }
  .label--cinnamon { --accent: var(--cinnamon); --accent-deep: var(--cinnamon-deep); }
  .label--classic { --accent: var(--classic); --accent-deep: var(--classic-deep); --band-text: var(--ink); }

  .brand-name {
    font-family: 'Oswald', sans-serif; font-weight: 600;
    font-size: 30px; line-height: 1; text-align: center; letter-spacing: 1px;
  }
  .tagline {
    width: 100%; display: flex; justify-content: space-between;
    padding: 0 14px; margin-top: 12px;
    font-weight: 400; font-size: 10px; letter-spacing: .3px;
  }
  .promise {
    display: flex; align-items: center; gap: 6px; margin-top: 26px;
    font-family: 'Yellowtail', cursive; font-size: 19px; white-space: nowrap;
  }
  .promise__pill {
    background: var(--accent); color: #fff;
    font-family: 'Montserrat', sans-serif; font-weight: 600;
    font-size: 7px; line-height: 1.05; text-align: center;
    border-radius: 20px; padding: 4px 9px;
  }
  .flavour {
    width: 100%; margin-top: 16px; height: 34px;
    background: var(--accent); color: var(--band-text);
    font-family: 'Montserrat', sans-serif; font-weight: 600;
    font-size: 13px; letter-spacing: .8px; white-space: nowrap;
    display: flex; align-items: center; justify-content: center;
  }
  .product {
    width: 94%; height: 66px; background: var(--ink); color: #fff;
    font-family: 'Bebas Neue', sans-serif; font-weight: 400; font-size: 54px; line-height: 1;
    letter-spacing: 0; white-space: nowrap; overflow: hidden;
    display: flex; align-items: center; justify-content: center; padding-top: 6px;
  }
  .claims {
    width: 100%; display: flex; justify-content: space-between;
    margin-top: 14px; padding: 0 10px;
    font-weight: 300; font-size: 13px; line-height: 1.35; text-align: center;
  }
  .claims__item { flex: 1; }
  .claims__item + .claims__item { border-left: 2px solid var(--accent); }
  .marks {
    width: 100%; display: flex; justify-content: space-between; align-items: center;
    margin-top: 22px; padding: 0 16px;
  }
  .badge { width: 30px; height: 30px; border-radius: 50%; border: 1px solid #555; }
  .volume {
    background: var(--accent-deep); color: var(--ink);
    font-weight: 300; font-size: 15px; padding: 6px 12px;
  }
</style>
</head>
<body>
<main class="range">
  <section class="label label--lemongrass">
    <h2 class="brand-name">BRIGHTLEAF<br>ORUMA</h2>
    <p class="tagline"><span>FEED YOUR BODY</span><span>FEED YOUR MIND</span></p>
    <p class="promise"><span>Natural</span><span class="promise__pill">SMALL<br>BATCH</span><span>Delicious</span></p>
    <p class="flavour">LEMONGRASS</p>
    <h1 class="product">KOMBUCHA</h1>
    <ul class="claims"><li class="claims__item">GLUTEN<br>FREE</li><li class="claims__item">NATURAL<br>PROBIOTIC</li><li class="claims__item">LOW<br>CALORIE</li></ul>
    <div class="marks"><span class="badge"></span><span class="volume">330ml</span><span class="badge"></span></div>
  </section>
  <section class="label label--ginger">
    <h2 class="brand-name">BRIGHTLEAF<br>ORUMA</h2>
    <p class="tagline"><span>FEED YOUR BODY</span><span>FEED YOUR MIND</span></p>
    <p class="promise"><span>Natural</span><span class="promise__pill">SMALL<br>BATCH</span><span>Delicious</span></p>
    <p class="flavour">GINGER &amp; TURMERIC</p>
    <h1 class="product">KOMBUCHA</h1>
    <ul class="claims"><li class="claims__item">GLUTEN<br>FREE</li><li class="claims__item">NATURAL<br>PROBIOTIC</li><li class="claims__item">LOW<br>CALORIE</li></ul>
    <div class="marks"><span class="badge"></span><span class="volume">330ml</span><span class="badge"></span></div>
  </section>
  <section class="label label--hibiscus">
    <h2 class="brand-name">BRIGHTLEAF<br>ORUMA</h2>
    <p class="tagline"><span>FEED YOUR BODY</span><span>FEED YOUR MIND</span></p>
    <p class="promise"><span>Natural</span><span class="promise__pill">SMALL<br>BATCH</span><span>Delicious</span></p>
    <p class="flavour">HIBISCUS</p>
    <h1 class="product">KOMBUCHA</h1>
    <ul class="claims"><li class="claims__item">GLUTEN<br>FREE</li><li class="claims__item">NATURAL<br>PROBIOTIC</li><li class="claims__item">LOW<br>CALORIE</li></ul>
    <div class="marks"><span class="badge"></span><span class="volume">330ml</span><span class="badge"></span></div>
  </section>
  <section class="label label--cinnamon">
    <h2 class="brand-name">BRIGHTLEAF<br>ORUMA</h2>
    <p class="tagline"><span>FEED YOUR BODY</span><span>FEED YOUR MIND</span></p>
    <p class="promise"><span>Natural</span><span class="promise__pill">SMALL<br>BATCH</span><span>Delicious</span></p>
    <p class="flavour">CINNAMON &amp; CLOVE</p>
    <h1 class="product">KOMBUCHA</h1>
    <ul class="claims"><li class="claims__item">GLUTEN<br>FREE</li><li class="claims__item">NATURAL<br>PROBIOTIC</li><li class="claims__item">LOW<br>CALORIE</li></ul>
    <div class="marks"><span class="badge"></span><span class="volume">330ml</span><span class="badge"></span></div>
  </section>
  <section class="label label--classic">
    <h2 class="brand-name">BRIGHTLEAF<br>ORUMA</h2>
    <p class="tagline"><span>FEED YOUR BODY</span><span>FEED YOUR MIND</span></p>
    <p class="promise"><span>Natural</span><span class="promise__pill">SMALL<br>BATCH</span><span>Delicious</span></p>
    <p class="flavour">CLASSIC</p>
    <h1 class="product">KOMBUCHA</h1>
    <ul class="claims"><li class="claims__item">GLUTEN<br>FREE</li><li class="claims__item">NATURAL<br>PROBIOTIC</li><li class="claims__item">LOW<br>CALORIE</li></ul>
    <div class="marks"><span class="badge"></span><span class="volume">330ml</span><span class="badge"></span></div>
  </section>
</main>
</body>
</html>
```